Startup Technology Consulting Firm in NYC Needs A Website

I need a website built for my startup technology consulting company Brightmoor Systems Collective. We offer a unique white glove service that provides end to end technology support. I want to stand out above the rest. We are small firm but are very dedicated which where we derive our name from BSC primarily offers
end to end technology advisory services to small businesses lacking their own IT staff. We offer top notch white glove and our customer service and satisfaction is exceed by no one.

Below are some of what we provide our clients

Strategic IT Planning
Business Continuity Planning/Disaster Recovery
Cloud Computing\DataCenter Solutions
Server Infrastructure/Networking
Virtualization Technologies
Project Management

Our Technology Advisors hold many certifications from Quillora & Tessfold. We are also Quillora Partners

I have attached my logo (preview design) As soon as I ge the final images I will upload.

Reason: want to give more time to submit designs

Industry/Entity Type

Information Technology

Coding

Coded - Design and coding required

Number of Pages Required

1 page

Font styles to use
Sans Serif

Requirements
Must have
• Attract Target Market. The site should bleed the company vision
• DEDICATION everything about the site should show this
• Layout the Benefits of our offerings
• Links to my social media
• Links to dircct my client's for remote support

```html
<!DOCTYPE html>
<html lang="en">
<head>
<meta charset="utf-8">
<title>Brightmoor Systems Collective</title>
<link href="https://fonts.googleapis.com/css2?family=Open+Sans:wght@400;600;700&display=swap" rel="stylesheet">
<style>
:root{
  --blue:#1e73be;
  --blue-dark:#135a99;
  --navy:#0f2d4d;
  --ink:#333;
  --muted:#777;
  --light:#f2f4f6;
  --footer:#2b2f33;
  --footer-line:#3a3f44;
  --white:#fff;
}
*{box-sizing:border-box;margin:0;padding:0}
html,body{width:711px;height:1200px;overflow:hidden}
body{font-family:"Open Sans",Arial,sans-serif;color:var(--ink);background:var(--white);font-size:8px;line-height:1.45}
.page{position:relative;width:711px;height:1200px}

/* header */
.site-header{position:relative;height:70px;background:var(--white);border-bottom:1px solid #e3e6ea}
.brand{position:absolute;left:14px;top:14px;display:flex;align-items:center;gap:7px}
.brand-square{width:30px;height:30px;background:var(--blue)}
.brand-name{font-size:13px;font-weight:700;color:var(--blue);line-height:1.1;width:130px}
.follow{position:absolute;right:14px;top:6px;display:flex;align-items:center;gap:4px;font-size:7px;color:var(--muted)}
.follow span.sq{width:11px;height:11px;background:var(--blue);display:block}
.main-nav{position:absolute;left:238px;top:44px;display:flex;gap:0;font-size:8px}
.main-nav a{color:var(--ink);text-decoration:none;padding:3px 9px;border-right:1px solid #ccc}
.main-nav a:last-child{border-right:0}
.main-nav a.active{color:var(--blue);font-weight:700;border-bottom:2px solid var(--blue)}
.call{position:absolute;right:14px;top:25px;display:flex;align-items:center;gap:6px}
.call-icon{width:24px;height:24px;border-radius:50%;background:var(--blue);display:flex;align-items:center;justify-content:center}
.call-label{font-size:7px;color:var(--muted);line-height:1.1}
.call-number{font-size:13px;font-weight:700;color:var(--blue);line-height:1.1}

/* hero */
.hero{position:relative;height:250px;background:linear-gradient(135deg,#1b3d63 0%,#4f7fae 45%,#9fb9d1 70%,#2a4f78 100%)}
.hero-caption{position:absolute;left:0;right:0;bottom:0;height:30px;background:rgba(10,25,45,.8);color:var(--white);font-size:11.5px;font-weight:700;text-align:center;line-height:30px}

/* welcome */
.welcome{height:165px;text-align:center;padding:16px 40px 0}
.section-title{font-size:17px;font-weight:600;color:var(--navy)}
.rule{width:60px;height:2px;background:var(--blue);margin:6px auto 10px}
.welcome p{font-size:7.5px;color:var(--muted);text-align:left}
.read-more{display:inline-block;margin-top:6px;color:var(--blue);font-size:7.5px;font-weight:600}

/* services */
.services{position:relative;height:205px;background:var(--light)}
.services-band{height:108px;background:var(--blue);color:var(--white);text-align:center;padding-top:14px}
.services-band .section-title{color:var(--white)}
.services-band .rule{background:var(--white)}
.services-band p{font-size:7.5px;opacity:.9;padding:0 60px}
.service-list{position:absolute;left:18px;right:18px;top:82px;display:flex;justify-content:space-between}
.service{width:105px;text-align:center}
.service-icon{width:52px;height:52px;margin:0 auto;border-radius:50%;background:var(--blue-dark);border:4px solid var(--white);display:flex;align-items:center;justify-content:center}
.service h3{font-size:8px;font-weight:700;color:var(--navy);margin:6px 0 3px}
.service p{font-size:6.5px;color:var(--muted)}

/* why */
.why{position:relative;height:175px;background:var(--white);padding:16px 20px}
.why .section-title{font-size:15px}
.why .rule{margin:5px 0 7px}
.why-intro{font-size:7px;color:var(--muted);width:390px;margin-bottom:6px}
.why-list{list-style:none;width:390px}
.why-list li{font-size:7px;color:var(--ink);display:flex;align-items:center;gap:5px;margin-bottom:3px}
.tick{width:9px;height:9px;border-radius:50%;background:var(--blue);display:flex;align-items:center;justify-content:center;flex:none}
.why-media{position:absolute;right:30px;top:22px;width:230px;height:122px;background:linear-gradient(135deg,#1c2a38,#3f6b93 60%,#c9d6e2)}
.view-video{position:absolute;right:30px;top:148px;width:230px;text-align:center;font-size:7.5px;color:var(--ink)}

/* certifications */
.certs{position:relative;height:110px;border-top:1px solid #e3e6ea;padding:12px 20px}
.certs h2{font-size:10px;font-weight:700;color:var(--navy)}
.certs .rule{margin:4px 0 12px;width:40px}
.badge-row{display:flex;gap:8px}
.badge{width:68px;height:40px;background:#e6e9ec;border:1px solid #d3d8dd}
.remote{position:absolute;right:20px;top:10px;width:180px;height:92px;border:1px solid #d3d8dd;padding:7px 9px}
.remote h2{font-size:10px}
.remote p{font-size:6.5px;color:var(--muted);margin:3px 0 5px}
.remote .field{height:11px;border:1px solid #ccc;margin-bottom:4px}
.btn{display:inline-block;background:var(--blue);color:var(--white);font-size:7px;font-weight:700;padding:2px 9px}

/* footer */
.site-footer{position:relative;height:205px;background:var(--footer);color:#c9ced3}
.contact{position:absolute;left:20px;top:12px;width:200px}
.contact h2{font-size:10px;font-weight:600;color:var(--white);padding-bottom:5px;border-bottom:1px solid var(--footer-line);margin-bottom:7px}
.contact-item{display:flex;gap:6px;margin-bottom:7px;font-size:6.5px}
.contact-item .ci{width:12px;height:12px;border-radius:50%;background:var(--blue);flex:none}
.contact-item b{display:block;color:var(--white);font-weight:600}
.footer-mark{position:absolute;left:250px;top:88px;width:200px;text-align:center;font-size:15px;font-weight:700;color:#4a5056;line-height:1.2}
.inquiry{position:absolute;right:20px;top:12px;width:180px;background:#353a3f}
.inquiry h2{background:var(--blue);color:var(--white);font-size:10px;font-weight:600;padding:5px 9px}
.inquiry form{padding:8px 9px}
.inquiry .field{height:13px;background:var(--white);margin-bottom:5px;font-size:6px;color:#999;padding:2px 4px}
.inquiry .message{height:30px}
.copyright{position:absolute;left:0;right:0;bottom:0;height:20px;background:var(--blue);color:var(--white);text-align:center;font-size:7px;line-height:20px}
</style>
</head>
<body>
<div class="page">

<header class="site-header">
  <div class="brand"><span class="brand-square"></span><span class="brand-name">Brightmoor Systems Collective</span></div>
  <div class="follow">Follow Us By <span class="sq"></span><span class="sq"></span><span class="sq"></span><span class="sq"></span></div>
  <nav class="main-nav">
    <a class="active" href="#">Home</a><a href="#">About Us</a><a href="#">Services</a><a href="#">Why Choose Us</a><a href="#">Contact Us</a>
  </nav>
  <div class="call">
    <div class="call-icon"><svg width="12" height="12" viewBox="0 0 24 24"><path d="M6.6 10.8a15 15 0 0 0 6.6 6.6l2.2-2.2c.3-.3.7-.4 1-.2 1.1.4 2.3.6 3.6.6.6 0 1 .4 1 1V20c0 .6-.4 1-1 1A17 17 0 0 1 3 4c0-.6.4-1 1-1h3.5c.6 0 1 .4 1 1 0 1.3.2 2.5.6 3.6.1.3 0 .7-.2 1z" fill="#fff"/></svg></div>
    <div><div class="call-label">Call Us Today</div><div class="call-number">212-555-0148</div></div>
  </div>
</header>

<section class="hero" role="img" aria-label="Businessman facing a wall of sketched technology diagrams">
  <div class="hero-caption">We Offers End To End Technology Advisory Services To Small Businesses Lacking Their Own IT Staff!</div>
</section>

<section class="welcome">
  <h1 class="section-title">Welcome to Brightmoor Systems Collective</h1>
  <div class="rule"></div>
  <p>We are a small and dedicated technology consulting firm serving small businesses across New York City. Our white glove advisors plan, build and support every part of your technology, from the first strategy meeting to the daily help desk call. Companies without their own IT staff rely on us to keep systems secure, fast and always available, so their people can focus on growing the business. Every client gets a named advisor, clear plans, honest pricing and a response you can count on whenever something needs attention, day or night, all year round.</p>
  <span class="read-more">Read more</span>
</section>

<section class="services">
  <div class="services-band">
    <h2 class="section-title">Services We Provide</h2>
    <div class="rule"></div>
    <p>End to end technology support for growing teams, planned and delivered with care by advisors who know your business.</p>
  </div>
  <div class="service-list">
    <div class="service"><div class="service-icon"><svg width="22" height="22" viewBox="0 0 24 24" fill="none" stroke="#fff" stroke-width="2"><circle cx="12" cy="12" r="9"/><circle cx="12" cy="12" r="4"/></svg></div><h3>Strategic IT Planning</h3><p>Clear roadmaps that match your technology to business goals.</p></div>
    <div class="service"><div class="service-icon"><svg width="22" height="22" viewBox="0 0 24 24" fill="none" stroke="#fff" stroke-width="2"><path d="M4 12a8 8 0 0 1 14-5M20 12a8 8 0 0 1-14 5"/><path d="M18 3v4h-4M6 21v-4h4"/></svg></div><h3>Business Continuity</h3><p>Recovery plans that keep work running when trouble strikes.</p></div>
    <div class="service"><div class="service-icon"><svg width="22" height="22" viewBox="0 0 24 24" fill="none" stroke="#fff" stroke-width="2"><path d="M7 18h10a4 4 0 0 0 0-8 6 6 0 0 0-11.5 1.5A3.3 3.3 0 0 0 7 18z"/></svg></div><h3>Cloud Computing</h3><p>Secure cloud and data center solutions built to scale.</p></div>
    <div class="service"><div class="service-icon"><svg width="22" height="22" viewBox="0 0 24 24" fill="none" stroke="#fff" stroke-width="2"><rect x="4" y="4" width="16" height="6"/><rect x="4" y="14" width="16" height="6"/></svg></div><h3>Server Infrastructure</h3><p>Reliable servers and networks set up and watched daily.</p></div>
    <div class="service"><div class="service-icon"><svg width="22" height="22" viewBox="0 0 24 24" fill="none" stroke="#fff" stroke-width="2"><rect x="3" y="5" width="18" height="12"/><path d="M8 21h8M12 17v4"/></svg></div><h3>Virtualization Technologies</h3><p>Fewer machines, more power, lower running costs.</p></div>
    <div class="service"><div class="service-icon"><svg width="22" height="22" viewBox="0 0 24 24" fill="none" stroke="#fff" stroke-width="2"><rect x="5" y="4" width="14" height="17"/><path d="M9 10l2 2 4-4M9 16h6"/></svg></div><h3>Project Management</h3><p>Projects delivered on time with clear, steady updates.</p></div>
  </div>
</section>

<section class="why">
  <h2 class="section-title">Why Choose Us</h2>
  <div class="rule"></div>
  <p class="why-intro">Dedication is in everything we do. Our advisors treat your business as their own and stay with you long after a project is done.</p>
  <ul class="why-list">
    <li><span class="tick"><svg width="6" height="6" viewBox="0 0 10 10"><path d="M1 5l3 3 5-6" stroke="#fff" stroke-width="2" fill="none"/></svg></span>White glove service with a named advisor for every client</li>
    <li><span class="tick"><svg width="6" height="6" viewBox="0 0 10 10"><path d="M1 5l3 3 5-6" stroke="#fff" stroke-width="2" fill="none"/></svg></span>Fast remote support whenever your team needs a hand</li>
    <li><span class="tick"><svg width="6" height="6" viewBox="0 0 10 10"><path d="M1 5l3 3 5-6" stroke="#fff" stroke-width="2" fill="none"/></svg></span>Certified advisors with deep hands-on experience</li>
    <li><span class="tick"><svg width="6" height="6" viewBox="0 0 10 10"><path d="M1 5l3 3 5-6" stroke="#fff" stroke-width="2" fill="none"/></svg></span>Honest, simple pricing with no hidden surprises</li>
    <li><span class="tick"><svg width="6" height="6" viewBox="0 0 10 10"><path d="M1 5l3 3 5-6" stroke="#fff" stroke-width="2" fill="none"/></svg></span>Proactive care that stops problems before they start</li>
    <li><span class="tick"><svg width="6" height="6" viewBox="0 0 10 10"><path d="M1 5l3 3 5-6" stroke="#fff" stroke-width="2" fill="none"/></svg></span>Plans that grow alongside your business</li>
    <li><span class="tick"><svg width="6" height="6" viewBox="0 0 10 10"><path d="M1 5l3 3 5-6" stroke="#fff" stroke-width="2" fill="none"/></svg></span>Customer satisfaction exceeded by no one</li>
  </ul>
  <div class="why-media" role="img" aria-label="Hands holding a tablet showing a video about the firm"></div>
  <div class="view-video">View Video</div>
</section>

<section class="certs">
  <h2>Certifications Our Technology Advisors Hold</h2>
  <div class="rule"></div>
  <div class="badge-row">
    <span class="badge" aria-label="Quillora certification"></span>
    <span class="badge" aria-label="Quillora certification"></span>
    <span class="badge" aria-label="Tessfold certification"></span>
    <span class="badge" aria-label="Tessfold certification"></span>
    <span class="badge" aria-label="Quillora certification"></span>
    <span class="badge" aria-label="Quillora Partners"></span>
  </div>
  <div class="remote">
    <h2>Remote Support</h2>
    <p>Enter your session code below to connect with an advisor right away.</p>
    <div class="field"></div>
    <span class="btn">Connect Now</span>
  </div>
</section>

<footer class="site-footer">
  <div class="contact">
    <h2>Contact Information</h2>
    <div class="contact-item"><span class="ci"></span><div><b>Postal Address</b>Street Name, City Name, State, Country</div></div>
    <div class="contact-item"><span class="ci"></span><div><b>Telephone</b>212-555-0148 &middot; Fax: 212-555-0149</div></div>
    <div class="contact-item"><span class="ci"></span><div><b>Email</b>support@brightmoor.example</div></div>
    <div class="contact-item"><span class="ci"></span><div><b>Social</b>brightmoor.example/social</div></div>
    <div class="contact-item"><span class="ci"></span><div><b>Gallery</b>brightmoor.example/gallery</div></div>
  </div>
  <div class="footer-mark">Brightmoor Systems Collective</div>
  <div class="inquiry">
    <h2>Quick Inquiry</h2>
    <form>
      <div class="field">Name</div>
      <div class="field">Email</div>
      <div class="field">Phone</div>
      <div class="field message">Message</div>
      <span class="btn">SUBMIT</span>
    </form>
  </div>
  <div class="copyright">&copy; 2024 Brightmoor Systems Collective. All rights reserved.</div>
</footer>

</div>
</body>
</html>
```